Quarlwick Builders Business Cards

I want to use the logo and make an unique business card that shows the textured Logo with brick and builings. I want to be able to stand out when I pass out business cards.

```html
<!DOCTYPE html>
<html lang="en">
<head>
<meta charset="utf-8">
<title>Quarlwick Builders Business Cards</title>
<link href="https://fonts.googleapis.com/css2?family=Oswald:wght@500;700&family=Montserrat:wght@400;700&display=swap" rel="stylesheet">
<style>
  :root {
    --bg: #7f7f7f;
    --terracotta: #c76a53;
    --terracotta-deep: #b55a44;
    --charcoal: #1d1d1d;
    --charcoal-soft: #2a2a2a;
    --accent: #e2553a;
    --white: #ffffff;
    --ink: #141414;
    --brand-dark: #3a1d14;
  }
  * { box-sizing: border-box; margin: 0; padding: 0; }
  html, body { width: 1200px; height: 800px; overflow: hidden; }
  body {
    background: var(--bg);
    font-family: "Montserrat", sans-serif;
    position: relative;
  }
  .card {
    position: absolute;
    top: 248px;
    width: 530px;
    height: 303px;
    border-radius: 14px;
    overflow: hidden;
    box-shadow: 0 6px 14px rgba(0,0,0,0.28);
  }
  .card--front {
    left: 50px;
    background: radial-gradient(ellipse at 30% 30%, var(--terracotta) 0%, var(--terracotta-deep) 100%);
  }
  .card--back {
    left: 620px;
    background: radial-gradient(ellipse at 60% 40%, var(--charcoal-soft) 0%, var(--charcoal) 100%);
  }
  .brand {
    position: absolute;
    font-family: "Oswald", sans-serif;
    font-weight: 700;
    text-transform: uppercase;
    line-height: 1;
    text-align: center;
  }
  .card--front .brand {
    left: 0; right: 0; top: 78px;
    font-size: 46px;
    letter-spacing: 1px;
    color: var(--brand-dark);
  }
  .card--back .brand {
    right: 34px; top: 34px;
    width: 250px;
    font-size: 34px;
    color: var(--accent);
  }
  .services-rule {
    position: absolute;
    left: 0; right: 0; top: 213px;
    height: 1px;
    background: rgba(255,255,255,0.8);
  }
  .services {
    position: absolute;
    left: 40px; right: 40px; top: 194px;
    height: 40px;
    background: var(--white);
    border-radius: 20px;
    display: flex;
    align-items: center;
    justify-content: center;
    gap: 8px;
    font-family: "Oswald", sans-serif;
    font-weight: 500;
    font-size: 21px;
    color: var(--ink);
  }
  .services .sep { color: var(--accent); }
  .person {
    position: absolute;
    left: 34px; top: 116px;
    color: var(--white);
  }
  .person__name {
    font-weight: 700;
    font-size: 24px;
    line-height: 1.2;
    letter-spacing: 0.5px;
    text-transform: uppercase;
  }
  .person__role {
    font-size: 14px;
    margin-top: 4px;
  }
  .contacts {
    list-style: none;
    margin-top: 10px;
    font-size: 13px;
  }
  .contacts li {
    display: flex;
    align-items: center;
    gap: 10px;
    height: 21px;
  }
  .icon { width: 13px; height: 13px; fill: var(--accent); flex: none; }
  .address {
    position: absolute;
    left: 300px; top: 128px;
    display: flex;
    gap: 8px;
    color: var(--white);
    font-size: 13px;
    line-height: 1.45;
  }
  .address .icon { margin-top: 2px; width: 14px; height: 14px; }
</style>
</head>
<body>

<section class="card card--front">
  <div class="brand">Quarlwick Builders</div>
  <div class="services-rule"></div>
  <div class="services">
    <span>Patios</span><span class="sep">-</span>
    <span>Sidewalks</span><span class="sep">-</span>
    <span>Retaining Walls</span><span class="sep">-</span>
    <span>Foundations</span>
  </div>
</section>

<section class="card card--back">
  <div class="brand">Quarlwick Builders</div>

  <div class="address">
    <svg class="icon" viewBox="0 0 24 24"><path d="M12 2a7 7 0 0 0-7 7c0 5 7 13 7 13s7-8 7-13a7 7 0 0 0-7-7zm0 9.5A2.5 2.5 0 1 1 12 6.5a2.5 2.5 0 0 1 0 5z"/></svg>
    <p>4417 Saltmarsh Bend Pkwy<br>212-B, FL 32408</p>
  </div>

  <div class="person">
    <p class="person__name">Delia Varrow</p>
    <p class="person__role">Founder &amp; CEO</p>
    <ul class="contacts">
      <li><svg class="icon" viewBox="0 0 24 24"><path d="M6.6 10.8a15 15 0 0 0 6.6 6.6l2.2-2.2c.3-.3.7-.4 1-.2 1.1.4 2.3.6 3.6.6.6 0 1 .4 1 1V20c0 .6-.4 1-1 1A17 17 0 0 1 3 4c0-.6.4-1 1-1h3.5c.6 0 1 .4 1 1 0 1.3.2 2.5.6 3.6.1.3 0 .7-.2 1z"/></svg>012-555-481-207</li>
      <li><svg class="icon" viewBox="0 0 24 24"><path d="M4 9c0-3 16-3 16 0v2h-4V9H8v2H4zm2 4h12l2 8H4zm6 2a2 2 0 1 0 0 4 2 2 0 0 0 0-4z"/></svg>044-555-390-162</li>
      <li><svg class="icon" viewBox="0 0 24 24"><path d="M2 12 22 3l-6 19-4-8z"/></svg>hello@quarlwick.com</li>
      <li><svg class="icon" viewBox="0 0 24 24"><path d="M12 2a10 10 0 1 0 0 20 10 10 0 0 0 0-20zm7.9 9h-3.9a15 15 0 0 0-1.3-6 8 8 0 0 1 5.2 6zM12 4c.9 1.2 1.8 3.6 2 7h-4c.2-3.4 1.1-5.8 2-7zM9.3 5a15 15 0 0 0-1.3 6H4.1a8 8 0 0 1 5.2-6zM4.1 13H8a15 15 0 0 0 1.3 6 8 8 0 0 1-5.2-6zM12 20c-.9-1.2-1.8-3.6-2-7h4c-.2 3.4-1.1 5.8-2 7zm2.7-1a15 15 0 0 0 1.3-6h3.9a8 8 0 0 1-5.2 6z"/></svg>www.quarlwick.com</li>
    </ul>
  </div>
</section>

</body>
</html>
```